Marrow Business Cards

Front of business card will have logo, name, address, & telephone number. Back of card will have a list of services provided - Roads, Substation Pads, Temporary Pads, Site Pads, Land Leveling, Powerline Row Cleaning, Land Clearing, Gates, Fencing, Construction Entrances, Excavation, Trenching, Underground Utilities, Directional Boring, Pile Driving. We are a construction company that uses heavy equipment like bulldozers, motor graders/blades, dump trucks, backhoes, hydro axes, & skid loaders. We build roads, pads, & install electric utility lines & waterlines underground. This logo is new. The word "Construction" can be smaller as uploaded 2 example edited logos. We will be using this card design for many employees.
Target Market(s)
Industrial Electric Powerline, Wind Turbine, Solar Panel, & Water Utility companies.
Contact Information for Business Card
Name/Position - Dorian Quale - Owner
Address: 4837 FM 582
Merkel, TX 79418
Phone number - (325) 418-2906

```html
<!DOCTYPE html>
<html lang="en">
<head>
<meta charset="utf-8">
<title>Marrow Construction Business Cards</title>
<link href="https://fonts.googleapis.com/css2?family=Josefin+Sans:wght@300;400;600;700&display=swap" rel="stylesheet">
<style>
  :root {
    --backdrop: #e9e9e9;
    --paper: #efefef;
    --maroon: #35111a;
    --grey-text: #8a8a8a;
    --light-text: #ece6e6;
  }
  * { margin: 0; padding: 0; box-sizing: border-box; }
  html, body {
    width: 1200px; height: 1200px; overflow: hidden;
    background: var(--backdrop);
    font-family: "Josefin Sans", sans-serif;
  }
  .card {
    position: absolute;
    left: 227px; width: 746px; height: 426px;
    display: flex; flex-direction: column; align-items: center;
  }
  .card--front { top: 135px; background: var(--paper); color: var(--maroon); }
  .card--back { top: 639px; background: var(--maroon); color: var(--light-text); }

  .wordmark {
    display: flex; flex-direction: column; align-items: center;
    font-weight: 700; line-height: 1;
    margin-top: 48px;
  }
  .wordmark__main { font-size: 66px; letter-spacing: 4px; }
  .wordmark__sub { font-size: 44px; letter-spacing: 3px; margin-top: 14px; }
  .card--back .wordmark { color: var(--light-text); margin-top: 52px; }

  .contact { text-align: center; margin-top: 50px; }
  .contact__name { font-size: 28px; font-weight: 600; letter-spacing: 1.5px; }
  .contact__role { font-size: 20px; font-weight: 300; color: var(--grey-text); margin-top: 6px; letter-spacing: 1px; }
  .contact__address { font-size: 20px; font-weight: 300; color: var(--grey-text); margin-top: 30px; letter-spacing: 1px; }
  .contact__phone { font-size: 20px; font-weight: 300; color: var(--grey-text); margin-top: 28px; letter-spacing: 1px; }
  .contact__phone b { color: var(--maroon); font-weight: 600; }

  .services {
    position: absolute; left: 31px; right: 26px; top: 276px;
    font-size: 21px; font-weight: 300; letter-spacing: 1px;
  }
  .services__row { display: flex; justify-content: space-between; height: 29.6px; }
</style>
</head>
<body>
  <section class="card card--front">
    <div class="wordmark">
      <span class="wordmark__main">MARROW</span>
      <span class="wordmark__sub">CONSTRUCTION</span>
    </div>
    <div class="contact">
      <p class="contact__name">DORIAN QUALE</p>
      <p class="contact__role">Owner</p>
      <p class="contact__address">4837 FM 582 Merkel, TX 79418</p>
      <p class="contact__phone"><b>P.</b> (325) 418-2906</p>
    </div>
  </section>

  <section class="card card--back">
    <div class="wordmark">
      <span class="wordmark__main">MARROW</span>
      <span class="wordmark__sub">CONSTRUCTION</span>
    </div>
    <div class="services">
      <div class="services__row"><span>•</span><span>Roads</span><span>•</span><span>Substation Pads</span><span>•</span><span>Temporary Pads</span><span>•</span><span>Site Pads</span></div>
      <div class="services__row"><span>•</span><span>Land Leveling</span><span>•</span><span>Powerline Row Cleaning</span><span>•</span><span>Land Clearing</span><span>•</span><span>Gates</span></div>
      <div class="services__row"><span>•</span><span>Fencing</span><span>•</span><span>Construction Entrances</span><span>•</span><span>Excavation</span><span>•</span><span>Trenching</span></div>
      <div class="services__row"><span>•</span><span>Underground Utilities</span><span>•</span><span>Directional Boring</span><span>•</span><span>Pile Driving.</span></div>
    </div>
  </section>
</body>
</html>
```